Tomas Whitlow Design, LLC (www.tomaswhitlow.design)

A very hip, trendy architectural home page. Simple Menu upper right hand corner (About, Projects, Inspiration, Design-Build, Contact). In the "Projects" ... I want to click on each project and that will open up multiple photo's of that project. Attached are the graphics of my logo. I want the home page to be incredible ... I really market my name "Tomas Whitlow" as sophisticated architecture. Colors/branding should be black/metallic/white/grey maybe with a pop of a bright color but not much. My architecture is like www.brennerfaulkatelier.com if you want to review as example. My specialty is industrial design, homes with architectural concrete design, steel beams, alot of glass. Very modern. My work is best illustrated at www.vasquerlind.com.
Updates

Please see images uploaded in my brief. A new business card design by an AWESOME designer and some inspirational architectural projects I worked on.

Industry/Entity Type

Architecture

Coding

Coded - Design and coding required

Number of Pages Required

5+ page

Colors

Designer to choose only greyscale colors for use in the design.

Requirements
Must have
• The 1st project photo gallery is called "Raw Dwelling at Cypress Point"... Images of this project can be taken from: https://www.homeplotra.com/homedetails/2817-9th-St-SE-Naples-FL-34117/508164229_zpid/

The 2nd project photo gallery is called "Stone, Iron and Timber Residence at Cypress Point". I will upload images for this project but use placeholder until I finalize.

The 3rd photo gallery is called "Early Sketches: Off the Page". I will forward pictures. for this.

Website should be easy to update and handover at completion as we will be updating frequently. Wordpress, WIX, or other type is fine as long as it looks profesional and high-class.
Nice to have
• Maybe the home page loads to just "Tomas Whitlow Design, LLC ... Atelier for Bold Structural Vision" and has a click to enter button. Something cool maybe a fade it or something eye-catching and cool.
Should not have
• Should not be overly colorful.

```html
<!DOCTYPE html>
<html lang="en">
<head>
<meta charset="utf-8">
<title>Tomas Whitlow Design, LLC</title>
<link href="https://fonts.googleapis.com/css2?family=Lato:wght@300;400;700;900&family=Oswald:wght@500;600&display=swap" rel="stylesheet">
<style>
:root{
  --accent:#e8641c;
  --ink:#1d1d1d;
  --text:#555;
  --muted:#9a9a9a;
  --line:#e4e4e4;
  --soft:#f4f4f4;
  --footer:#202020;
  --cream:#fbe6a6;
  --white:#fff;
}
*{margin:0;padding:0;box-sizing:border-box}
html,body{width:1200px;height:4952px;overflow:hidden}
body{position:relative;font-family:"Lato",sans-serif;color:var(--text);background:var(--white)}
.abs{position:absolute}
.ph{position:absolute;display:block}
.label{position:absolute;font-size:15px;color:var(--accent);font-weight:700;padding-left:12px}
.label::before{content:"";position:absolute;left:0;top:-6px;width:22px;height:2px;background:var(--accent)}
.btn{position:absolute;display:inline-flex;align-items:center;justify-content:center;background:var(--accent);color:#fff;font-size:14px;font-weight:700;border-radius:30px;height:40px;padding:0 28px}
h1,h2,h3{color:var(--ink);font-weight:400}

/* hero */
.hero{position:absolute;left:0;top:0;width:1200px;height:580px;background:linear-gradient(180deg,#2a2725 0%,#3b3530 45%,#1c1a18 100%)}
.topbar{position:absolute;left:0;top:0;width:1200px;height:28px;background:#111;color:#ccc;font-size:12px}
.topbar span{position:absolute;top:7px}
.brand{position:absolute;display:flex;align-items:center;gap:12px;font-size:18px;font-weight:700;color:#fff}
.brand i{display:block;width:30px;height:30px;border:2px solid currentColor}
.nav{position:absolute;left:590px;top:52px;display:flex;gap:8px;font-size:13px;color:#eee}
.nav a{padding:8px 14px;color:inherit;text-decoration:none}
.nav a.active{background:#fff;color:var(--ink)}
.hero-title{position:absolute;left:0;width:1200px;top:228px;text-align:center;font-family:"Oswald",sans-serif;font-weight:600;font-size:60px;line-height:68px;color:#fff}
.play{position:absolute;left:628px;top:390px;display:flex;align-items:center;gap:10px;color:#fff;font-size:14px;font-weight:700}
.play i{width:34px;height:34px;border-radius:50%;background:var(--accent);display:flex;align-items:center;justify-content:center}
.dots{position:absolute;left:968px;top:528px;display:flex;gap:6px}
.dots i{width:8px;height:8px;border-radius:50%;background:rgba(255,255,255,.5)}
.dots i:first-child{background:#fff}

/* about */
.about-frame{left:260px;top:640px;width:290px;height:420px;background:var(--cream);transform:skewX(-6deg)}
.about-photo{left:276px;top:662px;width:258px;height:380px;background:linear-gradient(180deg,#e9e4dc 0%,#e07a2d 55%,#9aa0a8 100%)}
.about h2{position:absolute;left:640px;top:810px;width:440px;font-size:28px;line-height:36px}
.about p{position:absolute;left:640px;top:900px;width:420px;font-size:13px;line-height:22px;color:var(--muted)}
.sign{left:640px;top:1010px;width:110px;height:40px;background:linear-gradient(90deg,#cfcfcf,#e6e6e6)}

/* project intro */
.proj h2{position:absolute;left:188px;top:1262px;width:400px;font-size:30px;line-height:40px}
.proj p{position:absolute;left:608px;top:1236px;width:400px;font-size:13px;line-height:22px;color:var(--muted)}

/* gallery */
.tile{position:absolute;box-shadow:0 8px 20px rgba(0,0,0,.15)}

/* blog */
.blog{position:absolute;left:0;top:2112px;width:1200px;height:888px;background:var(--soft)}
.blog h2{position:absolute;left:0;width:1200px;top:112px;text-align:center;font-size:30px;line-height:40px}
.blog h3{position:absolute;left:180px;top:410px;width:400px;font-size:19px;line-height:28px}
.blog p.lead{position:absolute;left:180px;top:478px;width:400px;font-size:13px;line-height:22px;color:var(--muted)}
.story{position:absolute;left:608px;width:440px;height:92px}
.story .ph{left:0;top:0;width:120px;height:92px}
.story p{position:absolute;left:140px;top:8px;width:290px;font-size:15px;line-height:24px;color:var(--ink)}

/* testimonial */
.testi h2{position:absolute;left:188px;top:3124px;font-size:28px}
.testi p.sub{position:absolute;left:188px;top:3170px;width:360px;font-size:13px;line-height:20px;color:var(--muted)}
.arrow{position:absolute;top:3130px;width:46px;height:46px;border-radius:50%;display:flex;align-items:center;justify-content:center}
.quote{position:absolute;left:220px;top:3390px;width:380px;font-size:13px;line-height:22px;color:var(--muted)}
.author{position:absolute;left:460px;top:3578px;font-size:16px;color:var(--ink)}
.qmark{position:absolute;left:604px;top:3282px;width:56px;height:56px;border-radius:50%;background:var(--accent);display:flex;align-items:center;justify-content:center;color:#fff;font-size:30px;font-weight:900}

/* contact */
.form{position:absolute;left:180px;top:3770px;width:440px;height:560px;background:#fff;box-shadow:0 10px 40px rgba(0,0,0,.1)}
.form h2{position:absolute;left:36px;top:40px;font-size:26px}
.form p{position:absolute;left:36px;top:84px;width:360px;font-size:12px;line-height:19px;color:var(--muted)}
.field{position:absolute;left:36px;width:360px;height:44px;border-bottom:1px solid var(--line);font-size:13px;color:#aaa;padding-top:16px}
.contact h2{position:absolute;left:658px;top:3850px;width:420px;font-size:32px;line-height:42px}
.contact p{position:absolute;left:658px;top:3952px;width:400px;font-size:17px;line-height:26px;color:var(--muted)}
.faq{position:absolute;left:658px;width:360px;height:40px;border-bottom:1px solid var(--line);font-size:14px;color:var(--ink);padding-top:12px}
.faq span{position:absolute;right:4px;top:10px;color:var(--accent);font-size:16px}

/* footer */
.footer{position:absolute;left:0;top:4380px;width:1200px;height:572px;background:var(--footer);color:#bbb;font-size:13px}
.footer h3{position:absolute;color:#fff;font-size:14px;font-weight:700}
.news{position:absolute;left:232px;top:90px;font-size:24px;color:#fff}
.news-input{position:absolute;left:640px;top:86px;width:244px;height:46px;background:#fff;font-size:12px;color:#aaa;padding:15px 16px}
.news-btn{position:absolute;left:884px;top:86px;width:50px;height:46px;background:var(--accent);display:flex;align-items:center;justify-content:center}
.fdiv{position:absolute;left:180px;top:176px;width:840px;height:1px;background:#3a3a3a}
.flist{position:absolute;list-style:none;line-height:24px}
.social{position:absolute;left:180px;top:420px;display:flex;gap:14px}
.social i{width:30px;height:30px;border-radius:50%;border:1px solid #888;display:block}
.copy{position:absolute;left:0;top:522px;width:1200px;padding-left:780px;font-size:12px;color:#888}
.copyline{position:absolute;left:0;top:500px;width:1200px;height:1px;background:#333}
</style>
</head>
<body>

<header class="hero">
  <span class="ph" role="img" aria-label="Modern glass and concrete house lit at dusk" style="left:0;top:0;width:1200px;height:580px;background:linear-gradient(180deg,rgba(60,52,45,.6),rgba(20,18,16,.8)),linear-gradient(90deg,#3a332c,#6a5a48 50%,#2c2824)"></span>
  <div class="topbar"><span style="left:680px">+01 555 777 1030</span><span style="left:850px">info@tomaswhitlow.design</span></div>
  <div class="brand" style="left:180px;top:48px"><i></i>Tomas Whitlow</div>
  <nav class="nav"><a class="active">Home</a><a>About</a><a>Projects</a><a>Inspiration</a><a>Design Build</a><a>Contact</a></nav>
  <h1 class="hero-title">Create The Building You<br>Want Here</h1>
  <span class="btn" style="left:464px;top:390px;height:36px;padding:0 22px">Read More</span>
  <div class="play"><i><svg width="12" height="12" viewBox="0 0 12 12"><path d="M3 1l8 5-8 5z" fill="#fff"/></svg></i>What's New</div>
  <div class="dots"><i></i><i></i><i></i></div>
</header>

<section class="about">
  <div class="abs about-frame"></div>
  <span class="ph about-photo" role="img" aria-label="Architect in hard hat and safety vest, arms crossed"></span>
  <span class="label" style="left:640px;top:784px">About</span>
  <h2>Elias Morrow is a principal and owner of Vasquer Lind,</h2>
  <p>In recent years, Elias has been awarded first place in multiple international design competitions, including The Harbor Gallery, The Lantern Children’s Museum, and Fairview Tower. His studio’s largest architectural competitions have earned wide acclaim across the world.</p>
  <span class="ph sign" role="img" aria-label="Handwritten signature"></span>
</section>

<section class="proj">
  <span class="label" style="left:188px;top:1234px">Project</span>
  <h2>In recent years, Elias has been awarded first place in multiple international design competitions, including</h2>
  <p>Team of architects, designers, visual artists and researchers have been winning public competitions, installations, sculpture, digital and graphic novels and film for over two decades. Ask the world of architecture and design with bold ideas.</p>
  <span class="btn" style="left:608px;top:1376px">Get Slide Show</span>
</section>

<section class="gallery">
  <span class="ph tile" role="img" aria-label="Curved glass atrium" style="left:0;top:1560px;width:292px;height:160px;background:linear-gradient(135deg,#a9b4bd,#6c7883)"></span>
  <span class="ph tile" role="img" aria-label="Modern interior with dark ceiling" style="left:320px;top:1500px;width:192px;height:248px;background:linear-gradient(160deg,#5a4a3a,#222)"></span>
  <span class="ph tile" role="img" aria-label="Grand staircase with red carpet" style="left:540px;top:1540px;width:332px;height:208px;background:linear-gradient(180deg,#c7a57a,#7a3a2a)"></span>
  <span class="ph tile" role="img" aria-label="White curved modern building" style="left:900px;top:1480px;width:188px;height:268px;background:linear-gradient(180deg,#8fb3d9,#d8d8d8)"></span>
  <span class="ph tile" role="img" aria-label="Lit building corner at night" style="left:1100px;top:1540px;width:100px;height:160px;background:linear-gradient(180deg,#2a3350,#8a6a40)"></span>
  <span class="ph tile" role="img" aria-label="Dark building detail" style="left:0;top:1760px;width:80px;height:100px;background:linear-gradient(180deg,#3a3028,#1a1a1a)"></span>
  <span class="ph tile" role="img" aria-label="Modern living room interior" style="left:108px;top:1760px;width:192px;height:260px;background:linear-gradient(160deg,#6a5848,#2a2420)"></span>
  <span class="ph tile" role="img" aria-label="Glass house at evening" style="left:320px;top:1780px;width:340px;height:180px;background:linear-gradient(180deg,#3f4a5c,#c08a4a)"></span>
  <span class="ph tile" role="img" aria-label="Hanging lights in a tall hall" style="left:680px;top:1760px;width:188px;height:260px;background:linear-gradient(180deg,#3a2a22,#a07040)"></span>
  <span class="ph tile" role="img" aria-label="Brick facade with windows" style="left:900px;top:1760px;width:300px;height:160px;background:linear-gradient(135deg,#8a4a30,#4a2a20)"></span>
</section>

<section class="blog">
  <span class="label" style="left:580px;top:84px">Blog</span>
  <h2>We guiding with passion lets<br>know our story</h2>
  <span class="ph" role="img" aria-label="Row of colourful old townhouses" style="left:180px;top:228px;width:408px;height:160px;background:linear-gradient(180deg,#8a9aa8,#7a5a48)"></span>
  <h3>We will help you to enjoy your architecture, films and graphic novels</h3>
  <p class="lead">At Vasquer Lind, Elias leads a team of designers with diverse skillsets. Under his leadership, the studio expands design studio campaigns and makes sustainability strategists and extraordinary visual artists, all united by a genuine collective spirit and goals.</p>
  <div class="story" style="top:228px"><span class="ph" role="img" aria-label="Skyscraper against sky" style="background:linear-gradient(180deg,#8ab0d0,#445566)"></span><p>For as long as he can remember, Vasquer Lind principal/owner</p></div>
  <div class="story" style="top:348px"><span class="ph" role="img" aria-label="Timber building facade" style="background:linear-gradient(180deg,#9aa4ac,#5a4a3c)"></span><p>He designs buildings, but also menu needs, installations, sculpture, landscapes, conceptual</p></div>
  <div class="story" style="top:468px"><span class="ph" role="img" aria-label="Concrete office tower" style="background:linear-gradient(180deg,#c8ccd0,#6a7078)"></span><p>At Vasquer Lind, Elias leads a team of designers with diverse skillsets.</p></div>
  <div class="story" style="top:600px"><span class="ph" role="img" aria-label="Modern lobby interior" style="background:linear-gradient(180deg,#b8a890,#4a4038)"></span><p>Sustainability strategists and extraordinary visual artists are all united by a genuine collective</p></div>
  <span class="btn" style="left:532px;top:782px">View More</span>
</section>

<section class="testi">
  <span class="label" style="left:188px;top:3100px">Testimonial</span>
  <h2>What our clients say about us</h2>
  <p class="sub">In recent years, Elias has been awarded first place in multiple international design competitions.</p>
  <span class="arrow" style="left:880px;background:#f0f0f0"><svg width="14" height="14" viewBox="0 0 14 14"><path d="M9 2L4 7l5 5" stroke="#999" stroke-width="2" fill="none"/></svg></span>
  <span class="arrow" style="left:960px;background:var(--accent)"><svg width="14" height="14" viewBox="0 0 14 14"><path d="M5 2l5 5-5 5" stroke="#fff" stroke-width="2" fill="none"/></svg></span>
  <p class="quote">Every step was handled with care and real attention to detail. The team listened to our goals and turned a simple idea into a home we love. Their sense of light, material and space is remarkable, and the process felt calm and clear from the first sketch to the final walkthrough. We would gladly work with them again.</p>
  <span class="author">-Jonah Dale</span>
  <span class="qmark">“</span>
  <span class="ph" role="img" aria-label="Black and white portrait of a client" style="left:640px;top:3248px;width:332px;height:420px;background:linear-gradient(160deg,#6a6a6a,#1a1a1a)"></span>
</section>

<section class="contact">
  <div class="form">
    <h2>Get In Touch</h2>
    <p>Leave us a short note about your project and we will reply within one working day to arrange a call.</p>
    <div class="field" style="top:176px">Name</div>
    <div class="field" style="top:230px">Mobile Number</div>
    <div class="field" style="top:284px">Enter your email ID</div>
    <div class="field" style="top:338px">Type of Message</div>
    <span class="btn" style="left:36px;top:460px">Send Message</span>
  </div>
  <span class="label" style="left:658px;top:3828px">Contact</span>
  <h2>If you have a question feel free to contact</h2>
  <p>Maybe your questions is have been answered, check this out</p>
  <div class="faq" style="top:4060px">What is Architectural home?<span>+</span></div>
  <div class="faq" style="top:4112px">What is Wood Finishes?<span>+</span></div>
  <div class="faq" style="top:4164px">What is the next upcoming project?<span>+</span></div>
  <span class="btn" style="left:658px;top:4224px">Contact Now</span>
</section>

<footer class="footer">
  <div class="news">Subscribe Our Newsletter</div>
  <div class="news-input">Enter your email</div>
  <div class="news-btn"><svg width="16" height="16" viewBox="0 0 16 16"><path d="M1 8l14-6-5 13-2-5z" fill="none" stroke="#fff" stroke-width="1.5"/></svg></div>
  <div class="fdiv"></div>
  <div class="brand" style="left:180px;top:264px;font-size:16px"><i></i>Tomas Whitlow</div>
  <div class="abs" style="left:180px;top:384px;color:#fff">Follow us</div>
  <div class="social"><i></i><i></i><i></i></div>
  <h3 style="left:468px;top:264px">Information</h3>
  <ul class="flist" style="left:468px;top:296px"><li>Home</li><li>About</li><li>Projects</li><li>Inspiration</li><li>Design Build</li><li>Blog</li></ul>
  <ul class="flist" style="left:612px;top:296px"><li>Contact</li><li>Features &amp; Benefits</li><li>Testimonial</li><li>Terms &amp; Conditions</li><li>Privacy &amp; Policy</li></ul>
  <h3 style="left:780px;top:264px">Contact Us</h3>
  <ul class="flist" style="left:780px;top:296px;width:220px"><li>2250 Harbor Crest Road</li><li>Suite 210, Naples FL 34102</li><li>info@tomaswhitlow.design</li><li>+01 555 777 1030</li></ul>
  <div class="copyline"></div>
  <div class="copy">© Tomas Whitlow Design, LLC. All Rights Reserved</div>
</footer>

</body>
</html>
```